I need graphics or illustrations to be used in a book and a power point presentation

I have created nine simple graphics using MS paint that were in blog articles. I now need to put these graphics in a book that I am publishing and also in a power point presentation.

I want these graphics to look more professional and consistent looking.

I have provided a word doc showing these graphics that need to be re-done

```html
<!DOCTYPE html>
<html lang="en">
<head>
<meta charset="UTF-8">
<title>The House of Israel – Timeline</title>
<link rel="stylesheet" href="https://fonts.googleapis.com/css2?family=Open+Sans:wght@400;600&display=swap">
<style>
  :root {
    --orange: #f7941d;
    --orange-light: #f9a63f;
    --orange-dark: #e07b12;
    --orange-fold: #b85f0a;
    --ink: #333333;
    --dash: #9a9a9a;
    --paper: #ffffff;
  }
  * { margin: 0; padding: 0; box-sizing: border-box; }
  html, body { width: 1200px; height: 720px; overflow: hidden; background: var(--paper); }
  body { font-family: "Open Sans", Arial, sans-serif; color: var(--ink); }

  .timeline-graphic { position: relative; width: 1200px; height: 720px; }
  .timeline-graphic svg.artwork { position: absolute; inset: 0; }

  .title-ribbon-text {
    position: absolute; left: 414px; top: 23px; width: 386px; height: 86px;
    display: flex; align-items: center; justify-content: center;
    color: #fff; font-size: 33px; font-weight: 400;
  }
  .dispensation-subtitle {
    position: absolute; left: 0; top: 205px; width: 1200px; text-align: center;
    color: var(--orange); font-size: 23px;
  }
  .year {
    position: absolute; top: 278px; width: 120px; margin-left: -60px; text-align: center;
    font-size: 27px; font-weight: 400;
  }
  .event-label {
    position: absolute; top: 490px; width: 170px;
    font-size: 17px; line-height: 1.38;
  }
  .era-bar {
    position: absolute; left: 103px; top: 614px; width: 663px; height: 64px;
    background: var(--orange-light);
    display: flex; align-items: center; justify-content: center;
    color: #fff; font-size: 23px;
  }
</style>
</head>
<body>
<main class="timeline-graphic">
  <svg class="artwork" width="1200" height="720" viewBox="0 0 1200 720" aria-hidden="true">
    <!-- title ribbon -->
    <polygon points="370,51 440,51 440,128 370,128 392,90" fill="var(--orange-dark)"/>
    <polygon points="844,51 774,51 774,128 844,128 822,90" fill="var(--orange-dark)"/>
    <polygon points="414,109 440,128 440,109" fill="var(--orange-fold)"/>
    <polygon points="800,109 774,128 774,109" fill="var(--orange-fold)"/>
    <rect x="414" y="23" width="386" height="86" fill="var(--orange)"/>

    <!-- timeline axis -->
    <line x1="114" y1="354" x2="1109" y2="354" stroke="var(--orange-light)" stroke-width="3"/>

    <!-- drop lines -->
    <g stroke="var(--dash)" stroke-width="2" stroke-dasharray="6 5">
      <line x1="114" y1="354" x2="114" y2="472"/>
      <line x1="363" y1="354" x2="363" y2="472"/>
      <line x1="620" y1="354" x2="620" y2="472"/>
      <line x1="831" y1="354" x2="831" y2="472"/>
      <line x1="1020" y1="354" x2="1020" y2="472"/>
    </g>

    <!-- milestone markers -->
    <g fill="var(--orange)">
      <circle cx="114" cy="354" r="15"/>
      <circle cx="363" cy="354" r="15"/>
      <circle cx="620" cy="354" r="15"/>
      <circle cx="1109" cy="354" r="15"/>
    </g>
  </svg>

  <div class="title-ribbon-text">The House of Israel</div>
  <p class="dispensation-subtitle">Dispensation of the "Gospel of Abraham"</p>

  <div class="year" style="left:114px">1836</div>
  <div class="year" style="left:363px">1837</div>
  <div class="year" style="left:620px">1840</div>

  <p class="event-label" style="left:103px">Waves of Conversion</p>
  <p class="event-label" style="left:352px">Foreign missions established-Gospel Taken from Gentiles to House of Israel</p>
  <p class="event-label" style="left:614px">Converts from the House of Israel begin flowing into Nauvoo</p>
  <p class="event-label" style="left:828px; width:150px">Succession Crisis</p>
  <p class="event-label" style="left:1014px">Converts from the House of Israel begin Flowing into Utah</p>

  <div class="era-bar">Gospel of Abraham Ushered in</div>
</main>
</body>
</html>
```